Quirky Label Design for an Exciting UK-Based Organic Skincare Company!

We need label designs across our range of products, we are a high quality yet quirky organic skincare company called Gently Lumora, we use frosted glass packaging, and we are just wanting one design done for now, but the winning designer we would want to work with to design the rest of the labels for us. We also want them to design business cards and other literature at some point and maybe even a website page.

Our label design will go on a 63mm tall frosted glass jar which is 62mm in diameter. The actual label dimensions should be, 170 mm (W) x 50 mm (H). The idea is so that it wraps around the whole jar with the design at one side (at the front) and the ingredients on another (at the back).

LABEL 1
Organic Polynesian Whipped Body Butter
Vanilla Bean
120ml

Made with Organic Shea and Cocoa Butters and exotic Monoi de Tahiti

Ingredients (INCI): Organic Raw Shea Butter (Butyrospermum Parkii), Organic Raw Cocoa Butter (Theobroma Cacao), Monoi de Tahiti (Coconut (Cocos nucifera) oil (and) Tiare (Gardenia tahitensis) flower), Organic Sweet Almond Oil (Prunus Amygdalus Dulcis), Organic Madagascan Vanilla Extract (Vanillin)

Handmade by Gently Lumora Ltd
14 Quillfield Lane, Bournemouth BH2 9RT, UK
Batch:

OPTIONAL WRITING (if it fits in):
100% Natural and Organic
Intensely Moisturising

LABEL 2
Mango Smoothie
120ml

Ingredients (INCI): Organic Raw Shea Butter (Butyrospermum Parkii), Organic Raw Cocoa Butter (Theobroma Cacao), Monoi de Tahiti (Coconut (Cocos nucifera) oil (and) Tiare (Gardenia tahitensis) flower), Organic Sweet Almond Oil (Prunus Amygdalus Dulcis), Organic Mango Flavour (Aroma)

Batch:

100% Natural and Organic
Intensely Moisturising

I have attached a picture of the jar we use and the lid we use for these products, as well as our logo. I've also attached a 'Handmade in Dorset' stamp which we'd like to go on there if possible, along with a shelf life symbol.

I am thinking the background colour of the labels will be either white or even brown paper colour. Perhaps it would be interesting to see it in both. UPDATE: We have decided on white background now, not brown.

The final design should denote handmade, organic, high quality, pure, yet quirky and original / unique. I am thinking perhaps a seemingly hand-drawn black leaf outline? Could fit the bill, but as I say, up to you. Something that says handmade yet professional.

I'd like to have the original Photoshop files from the winning designer so we can use them as a template for the rest of our horizontal labels.

Target Market(s)

Everyone that appreciates a good quality skincare product focusing on natural & organic. Price is mid-range to high

Industry/Entity Type

It Company

Requirements
Must have
• Must make the product look high quality & organic yet quirky and accessible. Must have our logo and the shelf life symbol and the writing as above.
Nice to have
• Nice to have the 'handmade' stamp attached, but not absolutely necessary if it doesn't fit within your design.

```html
<!DOCTYPE html>
<html lang="en">
<head>
<meta charset="utf-8">
<title>Gently Lumora – Whipped Body Butter Labels</title>
<link rel="stylesheet" href="https://fonts.googleapis.com/css2?family=Amatic+SC:wght@700&display=swap">
<style>
  :root {
    --bg: #e4e4e4;
    --label: #ffffff;
    --ink-grey: #7a7a7a;
    --rule-grey: #a9a9a9;
    --vanilla: #e8b923;
    --mango: #e53a3a;
    --badge-text: #ffffff;
  }
  * { box-sizing: border-box; margin: 0; padding: 0; }
  html, body { width: 1200px; height: 900px; overflow: hidden; }
  body {
    background: var(--bg);
    font-family: "Amatic SC", "Arial Narrow", sans-serif;
    font-weight: 700;
    position: relative;
  }
  .label {
    position: absolute;
    left: 80px;
    width: 1040px;
    height: 340px;
    background: var(--label);
    overflow: hidden;
  }
  .label--vanilla { top: 90px; }
  .label--mango { top: 470px; }

  .label__rules { position: absolute; inset: 0; }
  .label__rules path { fill: none; stroke: var(--rule-grey); stroke-width: 3; }

  .label__photo {
    position: absolute;
    left: 0; top: 46px;
    width: 330px; height: 266px;
  }
  .label--vanilla .label__photo {
    background: linear-gradient(160deg, #fbf8ee 0%, #f1ead0 55%, #6a4a32 100%);
  }
  .label--mango .label__photo {
    background: radial-gradient(circle at 45% 55%, #f8c63a 0%, #f3a526 55%, #e47a22 100%);
  }

  .brand {
    position: absolute;
    top: 22px;
    left: 400px;
    width: 260px;
    text-align: center;
    color: var(--ink-grey);
    font-size: 44px;
    line-height: 0.95;
    letter-spacing: 1px;
  }
  .brand__dot {
    display: inline-block;
    width: 10px; height: 10px;
    border-radius: 50%;
    background: var(--ink-grey);
    margin-right: 6px;
    vertical-align: middle;
  }

  .badge {
    position: absolute;
    top: 40px;
    left: 720px;
    width: 190px;
    padding: 7px 10px;
    border-radius: 6px;
    color: var(--badge-text);
    font-size: 26px;
    line-height: 1;
    text-align: center;
    transform: rotate(-4deg);
  }
  .label--vanilla .badge { background: var(--vanilla); }
  .label--mango .badge { background: var(--mango); }

  .product-name {
    position: absolute;
    top: 120px;
    left: 370px;
    width: 640px;
    text-align: center;
    font-size: 92px;
    line-height: 1;
    letter-spacing: 2px;
    white-space: nowrap;
  }
  .label--vanilla .product-name { color: var(--vanilla); }
  .label--mango .product-name { color: var(--mango); }

  .product-type {
    position: absolute;
    top: 226px;
    left: 470px;
    width: 440px;
    text-align: center;
    color: var(--ink-grey);
    font-size: 34px;
    line-height: 1.05;
    letter-spacing: 1px;
  }
</style>
</head>
<body>

<section class="label label--vanilla">
  <svg class="label__rules" width="1040" height="340" viewBox="0 0 1040 340" aria-hidden="true">
    <path d="M0 46 H380 C400 46 400 14 430 14 H630 C660 14 660 46 680 46 H1040"/>
    <path d="M0 314 H1040"/>
  </svg>
  <div class="label__photo" role="img" aria-label="Photograph of white vanilla orchid flowers and dark vanilla bean pods"></div>
  <div class="brand"><span class="brand__dot"></span>Gently<br>Lumora</div>
  <div class="badge">100% Natural<br>&amp; Organic</div>
  <h1 class="product-name">Vanilla Bean</h1>
  <p class="product-type">Organic Polynesian<br>Whipped Body Butter</p>
</section>

<section class="label label--mango">
  <svg class="label__rules" width="1040" height="340" viewBox="0 0 1040 340" aria-hidden="true">
    <path d="M0 46 H380 C400 46 400 14 430 14 H630 C660 14 660 46 680 46 H1040"/>
    <path d="M0 314 H1040"/>
  </svg>
  <div class="label__photo" role="img" aria-label="Photograph of a whole mango and a cubed mango half"></div>
  <div class="brand"><span class="brand__dot"></span>Gently<br>Lumora</div>
  <div class="badge">100% Natural<br>&amp; Organic</div>
  <h1 class="product-name">Mango Smoothie</h1>
  <p class="product-type">Organic Polynesian<br>Whipped Body Butter</p>
</section>

</body>
</html>
```